LumaMove In-home Personal Training

I would like to have some eye-catching business card design. Opened to any ideas.

The business idea: mobile fitness - train clients at their places

Target Market(s)

General population, 20-60 years old

Industry/Entity Type

Fitness

Contact Information for Business Card

The information to include:
Name: Marta
Call or text: 306-555-0187
Website: LumaMove.ca
Please use the attached logo

Requirements
Should not have
• No orange or purple colours please

```html
<!DOCTYPE html>
<html lang="en">
<head>
<meta charset="utf-8">
<title>LumaMove – Business Card</title>
<link href="https://fonts.googleapis.com/css2?family=Montserrat:wght@200;400;600&display=swap" rel="stylesheet">
<style>
  :root {
    --bg-top: #a3a3a3;
    --bg-bottom: #d4d4d4;
    --card: #333436;
    --ink: #f2f2f2;
    --ink-muted: #8e8f91;
  }
  * { margin: 0; padding: 0; box-sizing: border-box; }
  html, body { width: 1200px; height: 900px; overflow: hidden; }
  body {
    background: linear-gradient(180deg, var(--bg-top), var(--bg-bottom));
    font-family: "Montserrat", sans-serif;
    position: relative;
  }
  .card {
    position: absolute;
    top: 296px;
    width: 540px;
    height: 308px;
    background: var(--card);
    box-shadow: 0 6px 14px rgba(0,0,0,0.25);
    color: var(--ink);
  }
  .card--front { left: 40px; }
  .card--back { left: 620px; }

  .brand {
    position: absolute;
    left: 50%;
    top: 50%;
    transform: translate(-50%, -50%);
    display: flex;
    align-items: center;
    gap: 18px;
  }
  .brand__mark {
    width: 42px;
    height: 42px;
    border: 2px solid var(--ink);
    flex: none;
  }
  .brand__name {
    font-weight: 200;
    font-size: 44px;
    letter-spacing: 0.22em;
    line-height: 1;
  }
  .brand__tagline {
    margin-top: 8px;
    font-weight: 400;
    font-size: 9.5px;
    letter-spacing: 0.32em;
    color: var(--ink-muted);
    text-transform: uppercase;
  }

  .contact {
    position: absolute;
    left: 50%;
    top: 50%;
    transform: translate(-50%, -50%);
    display: flex;
    align-items: center;
    gap: 14px;
  }
  .contact__name {
    font-weight: 600;
    font-size: 30px;
  }
  .contact__divider {
    width: 1.5px;
    height: 44px;
    background: var(--ink);
  }
  .contact__list {
    list-style: none;
    font-weight: 400;
    font-size: 15px;
    line-height: 1.45;
  }
  .contact__item { display: flex; align-items: center; gap: 6px; }
  .contact__icon { width: 12px; height: 12px; flex: none; }
</style>
</head>
<body>
  <section class="card card--front">
    <div class="brand">
      <span class="brand__mark"></span>
      <div class="brand__text">
        <div class="brand__name">LumaMove</div>
        <div class="brand__tagline">In-home personal training</div>
      </div>
    </div>
  </section>

  <section class="card card--back">
    <div class="contact">
      <span class="contact__name">Marta</span>
      <span class="contact__divider"></span>
      <ul class="contact__list">
        <li class="contact__item">
          <svg class="contact__icon" viewBox="0 0 24 24" aria-hidden="true"><path fill="#f2f2f2" d="M6.6 10.8a15.1 15.1 0 0 0 6.6 6.6l2.2-2.2c.3-.3.7-.4 1-.2 1.1.4 2.3.6 3.6.6.6 0 1 .4 1 1V20c0 .6-.4 1-1 1C10.6 21 3 13.4 3 4c0-.6.4-1 1-1h3.5c.6 0 1 .4 1 1 0 1.3.2 2.5.6 3.6.1.3 0 .7-.2 1z"/></svg>
          306-555-0187
        </li>
        <li class="contact__item">
          <svg class="contact__icon" viewBox="0 0 24 24" aria-hidden="true" fill="none" stroke="#f2f2f2" stroke-width="2"><circle cx="12" cy="12" r="9"/><path d="M3 12h18M12 3c3 3 3 15 0 18M12 3c-3 3-3 15 0 18"/></svg>
          LumaMove.ca
        </li>
      </ul>
    </div>
  </section>
</body>
</html>
```